Business Card for a mobile physiotherapy company

I need a layout for a business card for a mobile physiotherapy company.
Slogan is "Mobile Physiotherapy - Your Road To Recovery"
Phone number is 867-402-5913
Email VantrePhysio@mailbright.ca (subject to change with website)
Website www.VantrePhysio.ca
My name and credentials: Kent Vantre Kent Vantre, BSc(kin), MPT, CAFCI, IMS
Information maybe included: Direct Billing, Services including Physiotherapy, IMS, acupuncture
Maybe include facebook and instagram logos
One side with the logo clean and sharp
Other side with details, try not to look too busy, keep everything concise

```html
<!DOCTYPE html>
<html lang="en">
<head>
<meta charset="utf-8">
<title>Vantre Therapy – Business Card</title>
<link href="https://fonts.googleapis.com/css2?family=Open+Sans:wght@400;600;700&display=swap" rel="stylesheet">
<style>
  :root {
    --navy: #16306a;
    --green: #0d4a3c;
    --ink: #222831;
    --rule: #7a7f86;
    --paper: #ffffff;
    --backdrop: #e6e7ea;
  }
  * { box-sizing: border-box; margin: 0; padding: 0; }
  html, body { width: 1200px; height: 977px; overflow: hidden; }
  body {
    background: var(--backdrop);
    font-family: "Open Sans", Arial, sans-serif;
    position: relative;
  }
  .card {
    position: absolute;
    left: 220px;
    width: 760px;
    height: 434px;
    overflow: hidden;
    box-shadow: 0 6px 18px rgba(0,0,0,0.18);
  }

  /* Front */
  .card-front { top: 40px; background: var(--navy); color: var(--paper); }
  .front-brand {
    position: absolute; top: 128px; left: 0; right: 0;
    display: flex; align-items: center; justify-content: center; gap: 18px;
    font-weight: 700; color: var(--paper);
  }
  .front-brand .mark { width: 26px; height: 26px; background: var(--paper); }
  .front-brand .name { font-size: 52px; letter-spacing: 6px; line-height: 1; text-transform: uppercase; }
  .front-brand .name small { display: block; font-size: 22px; letter-spacing: 17px; margin-top: 10px; }
  .slogan {
    position: absolute; top: 300px; left: 0; right: 0; text-align: center;
    font-size: 22px; font-weight: 700; letter-spacing: 0.3px;
  }

  /* Back */
  .card-back { top: 503px; background: var(--paper); color: var(--ink); }
  .back-brand {
    position: absolute; top: 96px; left: 70px;
    display: flex; align-items: center; gap: 12px;
    color: var(--navy); font-weight: 700; text-transform: uppercase;
  }
  .back-brand .mark { width: 16px; height: 16px; background: var(--navy); }
  .back-brand .name { font-size: 34px; letter-spacing: 4px; line-height: 1; }
  .back-brand .name small { display: block; font-size: 14px; letter-spacing: 11px; margin-top: 6px; }

  .holder { position: absolute; top: 100px; right: 92px; text-align: right; }
  .holder-name { color: var(--navy); font-size: 26px; font-weight: 700; }
  .holder-credentials { font-size: 14px; margin-top: 2px; }

  .divider { position: absolute; top: 192px; height: 2px; }
  .divider-grey { left: 90px; width: 405px; height: 1px; background: var(--rule); }
  .divider-navy { left: 495px; width: 180px; background: var(--navy); }

  .socials { position: absolute; top: 206px; left: 538px; list-style: none; font-size: 14px; }
  .socials li { display: flex; align-items: center; gap: 10px; height: 24px; }
  .socials .dot { width: 11px; height: 11px; background: var(--ink); border-radius: 2px; }

  .contacts { position: absolute; top: 280px; left: 96px; list-style: none; font-size: 15px; }
  .contacts li { display: flex; align-items: center; gap: 12px; height: 28px; }
  .contacts svg { width: 13px; height: 13px; fill: var(--green); }

  .band-navy { position: absolute; left: 0; bottom: 0; width: 555px; height: 24px; background: var(--navy); }
  .band-green { position: absolute; right: 0; bottom: 0; width: 190px; height: 34px; background: var(--green); }
</style>
</head>
<body>

<section class="card card-front" aria-label="Card front">
  <div class="front-brand">
    <span class="mark"></span>
    <span class="name">Vantre<small>Therapy</small></span>
  </div>
  <p class="slogan">Mobile Physiotherapy - Your Road To Recovery</p>
</section>

<section class="card card-back" aria-label="Card back">
  <div class="back-brand">
    <span class="mark"></span>
    <span class="name">Vantre<small>Therapy</small></span>
  </div>

  <div class="holder">
    <p class="holder-name">Kent Vantre</p>
    <p class="holder-credentials">BSc(kin), MPT, CAFCI, IMS</p>
  </div>

  <div class="divider divider-grey"></div>
  <div class="divider divider-navy"></div>

  <ul class="socials">
    <li><span class="dot"></span>VantrePhysio</li>
    <li><span class="dot"></span>VantrePhysio</li>
  </ul>

  <ul class="contacts">
    <li>
      <svg viewBox="0 0 24 24" aria-hidden="true"><path d="M6.6 10.8a15 15 0 0 0 6.6 6.6l2.2-2.2a1 1 0 0 1 1-.25 11.4 11.4 0 0 0 3.6.57 1 1 0 0 1 1 1V20a1 1 0 0 1-1 1A17 17 0 0 1 3 4a1 1 0 0 1 1-1h3.5a1 1 0 0 1 1 1c0 1.25.2 2.45.57 3.57a1 1 0 0 1-.25 1z"/></svg>
      867-402-5913
    </li>
    <li>
      <svg viewBox="0 0 24 24" aria-hidden="true"><path d="M2 5h20v14H2z M2 5l10 8 10-8" stroke="#fff" stroke-width="1.5"/></svg>
      VantrePhysio@mailbright.ca
    </li>
    <li>
      <svg viewBox="0 0 24 24" aria-hidden="true"><circle cx="12" cy="12" r="10"/><path d="M2 12h20M12 2c3 3 3 17 0 20M12 2c-3 3-3 17 0 20" stroke="#fff" stroke-width="1.5" fill="none"/></svg>
      www.VantrePhysio.ca
    </li>
  </ul>

  <div class="band-navy"></div>
  <div class="band-green"></div>
</section>

</body>
</html>
```